ultra-minimalist business card

front (black background, matte):

tarik b. hosseny
writer | photographer
get@tarikhosseny.com

back (white background, matte):

a picture speaks a thousand words;
a word draws a thousand pictures.

www.tarikhosseny.com

all text should be small (white or silver - as long as it shows against the black - on the front; black or gray - as long as it shows against the white - on the back).

feel free to get creative in terms of arrangement, alignment, and font type, but remember, the overall style is minimalist, so nothing too fancy, please.

thanks.

```html
<!DOCTYPE html>
<html lang="en">
<head>
<meta charset="utf-8">
<title>Tarik B. Hosseny — Business Card</title>
<link rel="stylesheet" href="https://fonts.googleapis.com/css2?family=Montserrat:wght@300;400;700;800&display=swap">
<style>
  :root {
    --backdrop: #d4d4d4;
    --card-black: #111111;
    --card-white: #ffffff;
    --ink-light: #f2f2f2;
    --ink-dark: #111111;
    --card-shadow: 0 6px 18px rgba(0,0,0,0.18);
  }
  * { margin: 0; padding: 0; box-sizing: border-box; }
  html, body {
    width: 1200px; height: 900px; overflow: hidden;
    background: var(--backdrop);
    font-family: "Montserrat", Arial, sans-serif;
  }
  .sheet {
    width: 1200px; height: 900px;
    display: flex; align-items: center; justify-content: center; gap: 40px;
  }
  .card {
    position: relative;
    width: 540px; height: 309px;
    box-shadow: var(--card-shadow);
    overflow: hidden;
  }

  /* front */
  .card--front { background: var(--card-black); color: var(--ink-light); }
  .name-frame {
    position: absolute; left: 170px; top: 112px;
    border: 2px solid var(--ink-light);
    padding: 9px 24px;
    font-weight: 400; font-size: 18px; letter-spacing: 0.3px;
    white-space: nowrap;
  }
  .contact-row {
    position: absolute; left: 170px; right: 40px; bottom: 44px;
    display: flex; justify-content: space-between; align-items: baseline;
    font-weight: 300; font-size: 13px; letter-spacing: 0.4px;
    white-space: nowrap;
  }

  /* back */
  .card--back { background: var(--card-white); color: var(--ink-dark); }
  .quote {
    position: absolute; left: 40px; top: 128px;
    display: flex; align-items: flex-start;
    font-size: 16px; font-weight: 300; line-height: 1.3; letter-spacing: 0.2px;
  }
  .quote strong { font-weight: 700; }
  .quote-mark {
    font-weight: 800; font-size: 36px; line-height: 1;
    height: 24px;
  }
  .quote-mark--open { margin-right: 10px; align-self: flex-end; margin-bottom: -4px; }
  .quote-mark--close { margin-left: 6px; margin-top: -8px; }
  .quote-lines { display: flex; flex-direction: column; }
  .quote-line { white-space: nowrap; }
  .quote-line--second { padding-left: 22px; }
  .website {
    position: absolute; right: 56px; bottom: 62px;
    font-weight: 300; font-size: 13px; letter-spacing: 0.4px;
  }
</style>
</head>
<body>
  <main class="sheet">
    <section class="card card--front" aria-label="Card front">
      <div class="name-frame">Tarik B. Hosseny</div>
      <div class="contact-row">
        <span class="role">writer | photographer</span>
        <span class="email">get@tarikhosseny.com</span>
      </div>
    </section>

    <section class="card card--back" aria-label="Card back">
      <blockquote class="quote">
        <span class="quote-mark quote-mark--open">&ldquo;</span>
        <span class="quote-lines">
          <span class="quote-line">a picture speaks <strong>a thousand words</strong>;</span>
          <span class="quote-line quote-line--second"><strong>a word draws</strong> a thousand pictures</span>
        </span>
        <span class="quote-mark quote-mark--close">&rdquo;</span>
      </blockquote>
      <p class="website">www.tarikhosseny.com</p>
    </section>
  </main>
</body>
</html>
```